Looking for fresh and exciting business card design that is simple and yet eye catching and impactfu

I am starting my own independent Marketing Communications consultancy with aim to service a small group of clients. Focus on aviation, travel and hospitality industries. Name of the consultancy is RQB BizLink or RQB Marketing Communications. Basic content of the card will be
RQB Marketing Communications / RQB BizLink
Greta Lund Okafor
Email
Mobile
Website

Target Market(s)

Aviation, travel and hospitality industries

Industry/Entity Type

Travel

Contact Information for Business Card

Greta Lund Okafor
Consultant
gretalok@mailbrook.example
Mobile : +86 1529 804 2617
Skype: gretabluepebble

Font styles to use
Sans Serif
Script

Requirements
Must have
• Professional look and feel.
Nice to have
• Fresh, contrast. I don't have a logo so using the company name to create a focal point.
Should not have
• Too many colors.

```html
<!DOCTYPE html>
<html lang="en">
<head>
<meta charset="utf-8">
<title>RQB BizLink – Business Card</title>
<link rel="stylesheet" href="https://fonts.googleapis.com/css2?family=Roboto:wght@400;500&family=Great+Vibes&display=swap">
<style>
  :root {
    --ink: #000000;
    --paper: #ffffff;
    --label-light: #e6e6e6;
    --label-dark: #8a8a8a;
    --shadow: rgba(0, 0, 0, 0.55);
  }
  html, body {
    margin: 0;
    padding: 0;
    overflow: hidden;
    background: var(--paper);
  }
  .card {
    position: relative;
    width: 1200px;
    height: 700px;
    background: var(--ink);
    overflow: hidden;
    font-family: "Roboto", Arial, sans-serif;
  }
  .info-panel {
    position: absolute;
    left: 208px;
    top: 214px;
    right: 0;
    bottom: 0;
    background: var(--paper);
    box-shadow: -6px -4px 14px var(--shadow);
  }
  .plane-icon {
    position: absolute;
    left: 52px;
    top: 59px;
    width: 143px;
    height: 91px;
  }
  .palm-art {
    position: absolute;
    left: 790px;
    top: 249px;
    width: 358px;
    height: 275px;
  }
  .brand-name {
    position: absolute;
    left: 0;
    width: 1200px;
    top: 30px;
    margin: 0;
    text-align: center;
    font-weight: 400;
    font-size: 100px;
    line-height: 1;
    color: var(--paper);
    text-shadow: 0 2px 0 #9a9a9a, 0 4px 6px rgba(255,255,255,0.25);
    letter-spacing: 1px;
  }
  .consultant-line {
    position: absolute;
    left: 0;
    width: 1200px;
    top: 128px;
    margin: 0;
    text-align: center;
    font-family: "Great Vibes", cursive;
    font-weight: 400;
    font-size: 74px;
    line-height: 1;
    color: var(--paper);
    white-space: nowrap;
  }
  .contact-list {
    position: absolute;
    left: 52px;
    top: 234px;
    margin: 0;
    padding: 0;
    list-style: none;
  }
  .contact-row {
    display: flex;
    align-items: baseline;
    height: 112px;
    font-size: 42px;
    line-height: 1;
    white-space: nowrap;
  }
  .contact-label {
    width: 162px;
    font-size: 44px;
    background: linear-gradient(180deg, var(--label-light) 10%, var(--label-dark) 95%);
    -webkit-background-clip: text;
    background-clip: text;
    color: transparent;
  }
  .contact-value {
    color: var(--ink);
    font-size: 40px;
  }
  .tagline {
    position: absolute;
    left: 276px;
    top: 594px;
    margin: 0;
    font-family: "Great Vibes", cursive;
    font-size: 84px;
    line-height: 1;
    color: var(--ink);
    white-space: nowrap;
  }
</style>
</head>
<body>
  <div class="card">
    <div class="info-panel"></div>

    <svg class="plane-icon" role="img" aria-label="Small white airplane icon" viewBox="0 0 143 91">
      <defs>
        <linearGradient id="planeTone" x1="0" y1="0" x2="0" y2="1">
          <stop offset="0" stop-color="#f2f2f2"/>
          <stop offset="1" stop-color="#c8c8c8"/>
        </linearGradient>
      </defs>
      <rect width="143" height="91" rx="10" fill="url(#planeTone)"/>
    </svg>

    <h1 class="brand-name">RQB BizLink</h1>
    <p class="consultant-line">Greta Lund Okafor; Consultant</p>

    <ul class="contact-list">
      <li class="contact-row"><span class="contact-label">Email:</span><span class="contact-value">gretalok@mailbrook.example</span></li>
      <li class="contact-row"><span class="contact-label">Mobile:</span><span class="contact-value">+86 1529 804 2617</span></li>
      <li class="contact-row"><span class="contact-label">Skype:</span><span class="contact-value">gretabluepebble</span></li>
    </ul>

    <svg class="palm-art" role="img" aria-label="Black silhouette of two palm trees on a small island" viewBox="0 0 358 275">
      <defs>
        <radialGradient id="palmTone" cx="0.5" cy="0.5" r="0.55">
          <stop offset="0" stop-color="#1a1a1a"/>
          <stop offset="0.75" stop-color="#444444"/>
          <stop offset="1" stop-color="#ffffff"/>
        </radialGradient>
      </defs>
      <rect width="358" height="275" fill="url(#palmTone)"/>
    </svg>

    <p class="tagline">Aviation, Travel, Hospitality</p>
  </div>
</body>
</html>
```